依頼詳細
・商品が増えたので新商品の案内 ギフト商品の紹介のチラシ(金額は入れません。)
・「こはるフルーツソース2本セット」を目玉として大きめに表示してください。
・商品の色を前面に出したデザインによる商品紹介
・文章はなるべく入れないで写真を強調した、シンプルでわかりやすいデザイン
・食品関連ギフトのチラシの作成経験者歓迎
・真空低温調理によるジャム製造のため、酸化も少なく、色が鮮やかなジャムに仕上がっています。
・自社農園産の果物を中心に、宮崎県産果物のみを使用。
・通常の手作業では実現できない品質をご提供することができます。
記載項目
「宝石のようなトロピカルジャム」という文言を必ず使用してください。

・こはるフルーツソース2本セット
「北海道産てんさい糖と宮崎県産フルーツのみを煮詰めたこだわりのソース」
内容:マンゴーソース  145g
パッションフルーツソース 145g

・こはるフルーツジャム6個セット
内容:マンゴージャム 150g
日向夏マーマレード 150g
きんかんマーマレード 150g
パイナップルジャム 150g
ブルーベリージャム 150g
パパイアジャム  150g

・こはるフルーツミニジャム6個セット
内容:マンゴージャム 50g
日向夏マーマレード 50g
きんかんマーマレード 50g
パイナップルジャム 50g
ブルーベリージャム 50g
パパイアジャム 50g

桐原白浜果樹株式会社
〒876-2231 宮崎県宮崎市桜丘町岩瀬2264番地
電話番号: 0985-47-2291
FAX:  0985-47-3356
サイズ
A4
ページ数
片面
希望イメージ
シンプル 複雑
単色 カラフル
暗い 明るい
日常 高級
遊び心 厳粛
未来的 伝統的
女性的 男性的
希望する色
納品ファイル
補足説明
■ 選んだ理由

シンプルで、しかも美味しさと高級感が伝わるようなデザインで、社内アンケートの結果一番評価が高かったので決めさせていただきました。

■ 提案者全員のお礼・コメント

たくさんのご提案をしていただき、選考には時間が
かかってしまい申し訳ありませんでした。どの方も素晴らしく、選ぶのにすごく悩みましたが、社内で検討し、一人の方を選ばせていただきました。
今回、初めて利用させていただきましたが、皆様のような素晴らしいデザイナーさんがいらっしゃるということが実感できましたので、また
利用させていただきたいと考えておりますので、今後ともどうぞよろしくお願いいたします。
本当にありがとうございました。

```html
<!DOCTYPE html>
<html lang="ja">
<head>
<meta charset="utf-8">
<title>New Gift Selection</title>
<link rel="stylesheet" href="https://fonts.googleapis.com/css2?family=Cormorant+Garamond:ital,wght@0,500;0,600;1,500&family=Noto+Serif+JP:wght@400;500;600&family=Noto+Sans+JP:wght@400;500&display=swap">
<style>
  :root {
    --paper: #ffffff;
    --ink: #1a1a1a;
    --muted: #555555;
    --accent: #d8521c;
    --band: #111111;
    --band-text: #f2f2f2;
    --amber: #c98a1e;
    --mango: #f2a516;
    --passion: #7a4a12;
    --plate: #e9dcc8;
    --jam-red: #8e1d1d;
  }
  * { margin: 0; padding: 0; box-sizing: border-box; }
  html, body { width: 879px; height: 1200px; overflow: hidden; background: var(--paper); }
  .flyer {
    position: relative; width: 879px; height: 1200px;
    background: var(--paper); color: var(--ink);
    font-family: "Noto Sans JP", sans-serif;
  }
  .flyer > * { position: absolute; }
  .title {
    top: 30px; left: 0; width: 100%; text-align: center;
    font-family: "Cormorant Garamond", serif; font-weight: 500;
    font-size: 50px; letter-spacing: 0.18em;
  }
  .subtitle {
    top: 95px; right: 120px;
    font-family: "Cormorant Garamond", serif; font-size: 17px; letter-spacing: 0.04em;
    color: var(--muted);
  }
  .photo { border-radius: 2px; }
  .photo-sauce {
    top: 130px; left: 60px; width: 200px; height: 410px;
    background: linear-gradient(90deg, var(--passion) 0%, var(--amber) 35%, #fff 48%, #fff 52%, var(--mango) 62%, #f6b940 100%);
  }
  .headline {
    top: 245px; left: 405px;
    font-family: "Noto Serif JP", serif; font-weight: 500; color: var(--accent);
    font-size: 52px; line-height: 1.2;
  }
  .headline span { display: block; }
  .headline span + span { margin-top: 4px; }
  .lead {
    top: 395px; left: 405px; width: 400px;
    font-size: 11.5px; line-height: 1.75; color: var(--muted);
  }
  .photo-pancake {
    top: 455px; left: 505px; width: 260px; height: 190px; border-radius: 50%;
    background: radial-gradient(ellipse at 50% 45%, #e2a850 0%, #b9752b 35%, var(--plate) 60%, #f7f2ea 100%);
  }
  .caption { font-size: 12px; line-height: 1.7; color: var(--muted); }
  .caption .name { font-family: "Noto Serif JP", serif; font-weight: 600; font-size: 15px; color: var(--ink); }
  .caption .weight { font-size: 11px; margin-left: 6px; color: var(--muted); font-weight: 400; }
  .caption-sauce { top: 555px; left: 60px; width: 380px; }
  .recipe-title {
    top: 605px; left: 60px;
    font-family: "Cormorant Garamond", serif; font-style: italic; font-weight: 500;
    font-size: 42px; letter-spacing: 0.04em;
  }
  .recipe-text { top: 662px; left: 60px; width: 430px; font-size: 11.5px; line-height: 1.75; color: var(--muted); }
  .photo-jam {
    top: 715px; left: 135px; width: 190px; height: 195px;
    background: linear-gradient(135deg, #f0b020 0%, #e27a18 30%, #5a3570 55%, #e8c040 75%, #c94a1a 100%);
  }
  .photo-mini {
    top: 705px; left: 485px; width: 280px; height: 210px;
    background: linear-gradient(135deg, var(--jam-red) 0%, #b83226 40%, #f0a830 60%, var(--jam-red) 100%);
  }
  .caption-jam { top: 925px; left: 60px; width: 380px; }
  .caption-mini { top: 925px; left: 485px; width: 360px; }
  .footer {
    top: 1040px; left: 0; width: 100%; height: 46px; background: var(--band); color: var(--band-text);
    display: flex; align-items: center; gap: 28px; padding: 0 60px; font-size: 12px;
  }
  .footer .company { font-family: "Noto Serif JP", serif; font-size: 15px; font-weight: 500; margin-right: 6px; }
</style>
</head>
<body>
<main class="flyer">
  <h1 class="title">New Gift Selection</h1>
  <p class="subtitle">from Miyazaki Kirihara Orchard</p>

  <div class="photo photo-sauce" role="img" aria-label="パッションフルーツソースとマンゴーソースの瓶2本の写真"></div>

  <h2 class="headline"><span>宝石のような</span><span>トロピカルジャム</span></h2>
  <p class="lead">自社農園産の果物を中心に宮崎県産果物のみを使用。真空低温調理で酸化が少なく、鮮やかな色のジャムに仕上げました。</p>

  <div class="photo-pancake" role="img" aria-label="フルーツソースをかけたパンケーキの写真"></div>

  <div class="caption caption-sauce">
    <p class="name">こはるフルーツソース 2本セット<span class="weight">(各145g)</span></p>
    <p>マンゴーソース / パッションフルーツソース</p>
  </div>

  <h3 class="recipe-title">Fruit Sauce Recipe</h3>
  <p class="recipe-text">北海道産てんさい糖と宮崎県産フルーツのみを煮詰めたこだわりのソース。<br>パンケーキやヨーグルト、アイスクリームにかけてお楽しみください。</p>

  <div class="photo photo-jam" role="img" aria-label="色とりどりのフルーツジャム6個セットの写真"></div>
  <div class="photo photo-mini" role="img" aria-label="赤い箱に入ったミニジャム6個セットの写真"></div>

  <div class="caption caption-jam">
    <p class="name">こはるフルーツジャム 6個セット<span class="weight">(各150g)</span></p>
    <p>マンゴージャム / 日向夏マーマレード / きんかんマーマレード<br>パイナップルジャム / ブルーベリージャム / パパイアジャム</p>
  </div>
  <div class="caption caption-mini">
    <p class="name">こはるフルーツミニジャム 6個セット<span class="weight">(各50g)</span></p>
    <p>マンゴージャム / 日向夏マーマレード / きんかんマーマレード<br>パイナップルジャム / ブルーベリージャム / パパイアジャム</p>
  </div>

  <footer class="footer">
    <span class="company">桐原白浜果樹株式会社</span>
    <span>〒876-2231 宮崎県宮崎市桜丘町岩瀬2264番地</span>
    <span>TEL 0985-47-2291</span>
    <span>FAX 0985-47-3356</span>
  </footer>
</main>
</body>
</html>
```